Fresh pet feed direct from manufacturer to door step. Quality and Freshness un-surpassed in Industr

Need Business Card Design; leading into many other projects, for New Franchised Business Opportunity providing home delivery of fresh dog and cat feed (no emphasis needed for cat) direct from manufacturing facility. (no middle men or distributors) Food is Farm to Factory fresh. Our trademarked tagline is "Quality is our MAIN Ingredient ! "
Updates

Please take note of other contest for Chirplane Cover and Profile Pic's

Target Market(s)

Dog and Cat owners

Industry/Entity Type

Pet

Contact Information for Business Card

Name, address, local phone, national 800 number, website, email address

Other font styles liked:
• follow that from logo

Requirements
Must have
• Our feed is made in Texas with ingredients sourced from local farms. We want to lean heavy on the Made in West Texas , ranch theme but that has a 'black label', 'vantrel', 'premium', 'high-end' look and feel
Nice to have
• maybe have an offer on card? 20% off with promo code "x" etc.. ?? just a thought...

```html
<!DOCTYPE html>
<html lang="en">
<head>
<meta charset="utf-8">
<title>Kestry's Premium – Business Card</title>
<link rel="stylesheet" href="https://fonts.googleapis.com/css2?family=Nunito+Sans:wght@400;800&display=swap">
<style>
  :root {
    --page: #ebeceb;
    --ink: #2a2828;
    --gold-edge: #9a6a28;
    --gold-mid: #d9a94a;
    --gold-light: #f5c860;
    --gold-rim: #8a5e22;
    --cream: #ffffff;
  }
  * { box-sizing: border-box; margin: 0; padding: 0; }
  html, body { width: 991px; height: 1200px; overflow: hidden; background: var(--page); }
  body { position: relative; font-family: "Nunito Sans", Arial, sans-serif; color: var(--ink); }

  .card {
    position: absolute; left: 89px; width: 785px; height: 471px;
    background: var(--ink); overflow: hidden;
    box-shadow: 0 0 0 1px #b8b8b8;
  }
  .card--front { top: 78px; }
  .card--back { top: 636px; }
  .card__art { position: absolute; inset: 0; width: 785px; height: 471px; }

  .brand {
    position: absolute; display: flex; align-items: center; justify-content: center;
    font-weight: 800; color: var(--ink); white-space: nowrap; letter-spacing: 1px;
  }
  .brand__dot { border-radius: 50%; background: var(--ink); flex: none; }
  .brand--large { left: 0; right: 0; top: 190px; gap: 14px; font-size: 52px; }
  .brand--large .brand__dot { width: 34px; height: 34px; }
  .brand--small { left: 30px; width: 215px; top: 86px; gap: 8px; font-size: 18px; }
  .brand--small .brand__dot { width: 14px; height: 14px; }

  .holder { position: absolute; left: 303px; top: 48px; }
  .holder__name { font-size: 37px; font-weight: 800; line-height: 1.15; }
  .holder__role { font-size: 32px; font-weight: 400; line-height: 1.2; }

  .contacts { position: absolute; left: 297px; top: 162px; list-style: none; }
  .contacts__item {
    display: flex; align-items: center; gap: 16px;
    height: 41.8px; font-size: 29px; font-weight: 400;
  }
  .contacts__icon { width: 28px; height: 28px; flex: none; }
</style>
</head>
<body>

<section class="card card--front" aria-label="Card front">
  <svg class="card__art" viewBox="0 0 785 471" aria-hidden="true">
    <defs>
      <linearGradient id="goldFront" x1="0" x2="1" y1="0" y2="0">
        <stop offset="0" stop-color="#9a6a28"/>
        <stop offset="0.25" stop-color="#d9a94a"/>
        <stop offset="0.5" stop-color="#f5c860"/>
        <stop offset="0.75" stop-color="#d9a94a"/>
        <stop offset="1" stop-color="#9a6a28"/>
      </linearGradient>
    </defs>
    <path d="M0,0 H785 V253 Q392,625 0,253 Z" fill="#ffffff"/>
    <path d="M0,0 H785 V253 Q392,619 0,253 Z" fill="#8a5e22"/>
    <path d="M0,0 H785 V250 Q392,613 0,250 Z" fill="url(#goldFront)"/>
  </svg>
  <div class="brand brand--large"><span class="brand__dot"></span>KESTRY'S PREMIUM</div>
</section>

<section class="card card--back" aria-label="Card back">
  <svg class="card__art" viewBox="0 0 785 471" aria-hidden="true">
    <defs>
      <linearGradient id="goldBack" x1="0" x2="1" y1="0" y2="0">
        <stop offset="0" stop-color="#9a6a28"/>
        <stop offset="0.25" stop-color="#d9a94a"/>
        <stop offset="0.5" stop-color="#f5c860"/>
        <stop offset="0.75" stop-color="#d9a94a"/>
        <stop offset="1" stop-color="#9a6a28"/>
      </linearGradient>
    </defs>
    <path d="M0,0 H785 V251 Q392,621 0,251 Z" fill="#ffffff"/>
    <path d="M0,0 H785 V251 Q392,615 0,251 Z" fill="#8a5e22"/>
    <path d="M0,0 H785 V248 Q392,609 0,248 Z" fill="url(#goldBack)"/>
  </svg>

  <div class="brand brand--small"><span class="brand__dot"></span>KESTRY'S PREMIUM</div>

  <div class="holder">
    <p class="holder__name">Your Name</p>
    <p class="holder__role">Position</p>
  </div>

  <ul class="contacts">
    <li class="contacts__item">
      <svg class="contacts__icon" viewBox="0 0 24 24"><path d="M6.5 3 L9.5 3 L10.5 8 L8.3 9.6 Q10 13.8 14.4 15.7 L16 13.5 L21 14.5 L21 17.5 Q20 21 16.5 20.5 Q5 18 3.5 7.5 Q3.2 4 6.5 3 Z" fill="#2a2828"/></svg>
      <span>123-456-7890</span>
    </li>
    <li class="contacts__item">
      <svg class="contacts__icon" viewBox="0 0 24 24"><rect x="6" y="2.5" width="12" height="19" rx="2" fill="none" stroke="#2a2828" stroke-width="1.8"/><circle cx="12" cy="18.3" r="1" fill="#2a2828"/></svg>
      <span>123-456-7888</span>
    </li>
    <li class="contacts__item">
      <svg class="contacts__icon" viewBox="0 0 24 24"><rect x="2.5" y="6" width="19" height="12" fill="none" stroke="#2a2828" stroke-width="1.8"/><path d="M2.5 6 L12 13 L21.5 6 M2.5 18 L9.5 11.5 M21.5 18 L14.5 11.5" fill="none" stroke="#2a2828" stroke-width="1.6"/></svg>
      <span>name@kestryspremium.com</span>
    </li>
    <li class="contacts__item">
      <svg class="contacts__icon" viewBox="0 0 24 24"><g fill="none" stroke="#2a2828" stroke-width="1.6"><circle cx="12" cy="12" r="9.5"/><ellipse cx="12" cy="12" rx="4" ry="9.5"/><path d="M2.5 12 H21.5 M4 7 H20 M4 17 H20 M12 2.5 V21.5"/></g></svg>
      <span>www.kestryspremium.com</span>
    </li>
    <li class="contacts__item">
      <svg class="contacts__icon" viewBox="0 0 24 24"><path d="M2.5 11 L12 4.5 L21.5 11 Z" fill="#2a2828"/><rect x="4.5" y="11" width="15" height="8.5" fill="none" stroke="#2a2828" stroke-width="1.8"/><rect x="10" y="13.5" width="4" height="6" fill="#2a2828"/></svg>
      <span>address</span>
    </li>
    <li class="contacts__item">
      <svg class="contacts__icon" viewBox="0 0 24 24"><rect x="3" y="3" width="18" height="18" rx="2" fill="none" stroke="#2a2828" stroke-width="1.8"/></svg>
      <span>chirplane</span>
    </li>
  </ul>
</section>

</body>
</html>
```